DOUBLE SIDED BROCHURE NEEDED TO PROMOTE DOCTOR

I need a double sided DL size (99mm x 210mm) brochure, promoting a doctor seeing patients in a new area.

I want something professional. I have included the relevant information. I would also like the Dr's picture somwhere in the brochure, with a professional background. I wish to print these tomorrow, so i will pick a winner within 14 hours of posting this ad.

I have included an example of a brochures design that I recently saw, and its definietly a good starting point.

Medical

```html
<!DOCTYPE html>
<html lang="en">
<head>
<meta charset="utf-8">
<title>Dr. Sami Haddad – DL Brochure</title>
<link href="https://fonts.googleapis.com/css2?family=Jost:wght@400;500&family=Tinos:ital,wght@0,700;1,700&display=swap" rel="stylesheet">
<style>
  :root {
    --backdrop: #a3a2a7;
    --ink: #1b1d1f;
    --white: #ffffff;
    --green: #17a56f;
    --teal: #4f9c9e;
    --teal-soft: #8fc3c4;
    --pale: #eef5f6;
    --gold: #d8b636;
    --photo-dark: #2b2d33;
    --photo-light: #8a8f99;
  }
  * { margin: 0; padding: 0; box-sizing: border-box; }
  html, body { width: 1200px; height: 900px; overflow: hidden; }
  body {
    background: var(--backdrop);
    position: relative;
    font-family: "Jost", sans-serif;
    color: var(--ink);
  }
  .panel {
    position: absolute;
    top: 70px;
    width: 358px;
    height: 760px;
    overflow: hidden;
    box-shadow: 0 6px 18px rgba(0,0,0,0.25);
  }

  /* ---------- Reverse side ---------- */
  .panel--info {
    left: 200px;
    background: linear-gradient(180deg, var(--white) 0%, var(--pale) 22%, var(--teal-soft) 60%, var(--teal) 100%);
    padding: 28px 24px;
    font-size: 14.5px;
    line-height: 1.3;
  }
  .info__lead {
    text-align: center;
    font-weight: 500;
    font-size: 15.5px;
    letter-spacing: 0.3px;
    margin-bottom: 22px;
  }
  .info__intro { text-align: center; font-size: 14px; margin-bottom: 14px; }
  .info__list {
    list-style: none;
    display: grid;
    grid-template-columns: 1fr 1fr;
    column-gap: 8px;
    row-gap: 2px;
    font-size: 11.5px;
    margin-bottom: 10px;
  }
  .info__list .wide { grid-column: 1 / -1; }
  .info__sub { font-size: 11.5px; margin-bottom: 2px; }
  .clinic {
    margin-top: 30px;
    text-align: center;
  }
  .clinic__name { font-size: 22px; font-weight: 400; }
  .clinic__mark {
    display: block;
    margin: 10px auto 22px;
    width: 56px;
    height: 56px;
    border-radius: 50%;
    background: var(--ink);
  }
  .clinic__address { font-size: 13px; line-height: 1.35; }
  .referral {
    margin-top: 16px;
    font-size: 17px;
    font-weight: 500;
    line-height: 1.3;
  }

  /* ---------- Front side ---------- */
  .panel--cover {
    left: 642px;
    background: linear-gradient(180deg, var(--green) 0%, var(--teal) 70%, var(--teal) 100%);
  }
  .cover__wave { position: absolute; inset: 0; }
  .cover__emblem {
    position: absolute;
    top: 16px;
    left: 159px;
    width: 40px;
    height: 40px;
    border-radius: 50%;
    background: var(--gold);
  }
  .cover__title {
    position: absolute;
    top: 82px;
    width: 100%;
    text-align: center;
    font-family: "Tinos", serif;
    font-weight: 700;
    font-size: 29px;
    line-height: 1.15;
    color: var(--ink);
  }
  .cover__announce {
    position: absolute;
    top: 190px;
    left: 28px;
    right: 24px;
    font-family: "Tinos", serif;
    font-weight: 700;
    font-size: 20px;
    line-height: 1.15;
    color: var(--white);
  }
  .cover__name {
    position: absolute;
    top: 500px;
    left: 40px;
    font-family: "Tinos", serif;
    font-style: italic;
    font-weight: 700;
    font-size: 19px;
    color: var(--ink);
  }
  .cover__photo {
    position: absolute;
    right: 0;
    bottom: 0;
    width: 250px;
    height: 230px;
    background: radial-gradient(ellipse at 50% 35%, var(--photo-light) 0%, var(--photo-dark) 75%);
  }
</style>
</head>
<body>

  <section class="panel panel--info">
    <p class="info__lead">Guaranteed appointment within two weeks, with patients having the option of surgery at Lakeside Health Campus, Southgate General Hospital or St. Anne's Private Hospital.</p>

    <p class="info__intro">Dr. Haddad is a highly trained specialist surgeon, in all areas of Endocrine, Breast and General Surgery. Including:</p>

    <ul class="info__list">
      <li class="wide">- Thyroid Surgery</li>
      <li class="wide">- Parathyroid surgery (including minimally invasive parathyroidectomy)</li>
      <li>- Breast Cancer</li>
      <li>- Benign breast disease</li>
    </ul>

    <p class="info__sub">All areas of general surgery, such as;</p>
    <ul class="info__list">
      <li>-Gallbladder surgery</li>
      <li>-Hernia surgery</li>
      <li>-Haemorrhoid</li>
      <li>-Vasectomy</li>
    </ul>

    <div class="clinic">
      <p class="clinic__name">Bayview Clinic</p>
      <span class="clinic__mark" role="img" aria-label="Clinic emblem"></span>
      <p class="clinic__address">42 Harbour Crest Road<br>Bayview WA 6199.<br>Phone: 1300 555 014</p>
    </div>

    <p class="referral">Please send all referrals by fax to (08) 5550 1482.</p>
  </section>

  <section class="panel panel--cover">
    <svg class="cover__wave" viewBox="0 0 358 760" preserveAspectRatio="none" aria-hidden="true">
      <path d="M358 400 C 250 430, 160 470, 70 540 C 30 570, 10 600, 0 620 L0 700 C 40 720, 80 740, 100 760 L358 760 Z" fill="#ffffff"/>
    </svg>
    <span class="cover__emblem" role="img" aria-label="Medical emblem"></span>
    <h1 class="cover__title">The Doctor<br>Will See You Now</h1>
    <p class="cover__announce">We are pleased to announce that Dr. Sami Haddad is now consulting in Bayview, seeing public and private patients.</p>
    <p class="cover__name">Dr. Sami Haddad</p>
    <div class="cover__photo" role="img" aria-label="Portrait photograph of Dr. Sami Haddad in a dark suit"></div>
  </section>

</body>
</html>
```